Vitamin B12 Liquid Drops Label

hi, i need a label designed for my vitamin b12 drops that i am going to be selling on bazaroo. the label needs to quickly capture the attention of a buyer as he or she is scrolling through the thumbnail search results on bazaroo.example my brand is called zulpa. i already have an example brand logo i will be using, however, i need help designing the rest of the label. attached are some examples of labels i like for other supplements.some of these examples are pink. i do not want pink. please go for a blue/green color scheme. THE DESIGN MUST BE BOLD

Target Market(s)

adults ages 30 - 64

Font styles to use
Sans Serif

Colors
0455a3
cedeed
3176b5
85acd3
cfdeed
9bcb3b
abd037
cadf82
00a990

Requirements
Must have
• - bold design
• - somewhat gender-neutral color scheme because this will be used equally by men and women
• - B12 MUST be very prominent and visible on the label
Should not have
• - it should not be "crunchy" looking

```html
<!DOCTYPE html>
<html lang="en">
<head>
<meta charset="utf-8">
<title>Zulpa Vitamin B12 Drops – Packaging</title>
<link rel="stylesheet" href="https://fonts.googleapis.com/css2?family=Fredoka:wght@500;600;700&display=swap">
<style>
  :root {
    --backdrop: #cedeed;
    --navy: #0455a3;
    --mid-blue: #3176b5;
    --sky: #85acd3;
    --lime: #9bcb3b;
    --lime-bright: #abd037;
    --lime-pale: #cadf82;
    --teal: #00a990;
  }
  html, body {
    margin: 0;
    padding: 0;
    width: 1200px;
    height: 800px;
    overflow: hidden;
    background: var(--backdrop);
    font-family: "Fredoka", Arial, sans-serif;
  }
  .stage {
    position: relative;
    width: 1200px;
    height: 800px;
  }
  .carton-front {
    position: absolute;
    left: 210px;
    top: 100px;
    width: 320px;
    height: 620px;
  }
  .drop-label {
    position: absolute;
    left: 640px;
    top: 160px;
    width: 390px;
    height: 500px;
  }
  svg text { font-family: "Fredoka", Arial, sans-serif; }
  .brand-mark { font-weight: 700; fill: var(--navy); }
  .carton-title { font-weight: 600; fill: var(--lime-pale); letter-spacing: 2px; }
  .label-hero { font-weight: 700; fill: var(--navy); }
  .label-spec { font-weight: 600; fill: var(--lime-pale); }
  .label-brand { font-weight: 600; fill: var(--lime-bright); }
</style>
</head>
<body>
<main class="stage">

  <svg class="carton-front" viewBox="0 0 320 620" aria-label="Zulpa Vitamin B12 carton front">
    <rect class="carton-base" x="0" y="0" width="320" height="620" fill="var(--lime)"/>
    <rect class="carton-top-strip" x="0" y="0" width="320" height="42" fill="var(--sky)"/>
    <polygon class="carton-band" points="0,365 320,225 320,350 0,445" fill="var(--navy)"/>
    <polygon class="carton-lower-band" points="0,490 320,560 320,620 300,620 0,550" fill="var(--teal)"/>
    <text class="brand-mark" x="30" y="300" font-size="74" transform="rotate(-24 30 300)">ZULPA</text>
    <text class="carton-title" x="30" y="420" font-size="46" transform="rotate(-24 30 420)">VITAMIN B12</text>
  </svg>

  <svg class="drop-label" viewBox="0 0 390 500" aria-label="Zulpa B12 dropper bottle label">
    <rect class="label-base" x="0" y="0" width="390" height="500" fill="var(--navy)"/>
    <polygon class="label-lime-field" points="0,0 390,0 320,260 0,260" fill="var(--lime)"/>
    <text class="label-hero" x="16" y="200" font-size="148">B12</text>
    <text class="label-spec" x="22" y="310" font-size="30">5000 MCG*</text>
    <text class="label-spec" x="22" y="356" font-size="32" letter-spacing="6">METHYL</text>
    <text class="label-spec" x="22" y="388" font-size="18" letter-spacing="7">COBAMALIN</text>
    <text class="label-spec" x="22" y="448" font-size="24">MADE IN</text>
    <text class="label-spec" x="26" y="482" font-size="24" letter-spacing="18">USA</text>
    <text class="label-brand" x="368" y="468" font-size="46" text-anchor="end">ZULPA</text>
  </svg>

</main>
</body>
</html>
```